Stationery Design Project - Red Fern Workforce

Red Fern Workforce Staff
*Calder *Ridgeford

Business Cards
Size: 90mm x 55mm
Letterhead
Size: A4 - 210mm x 297mm
With Compliments Slip
Size: DL - 210mm x 99mm
Notepad
Size: 250mm x 140mm
Presentation Folder
Size: A4

Phone: 08 9417 2630
Email: info@redfernworkforce.com.au
website: www.redfernworkforce.com.au
Address: 147 Tolmer Road
Harrowdene Coastal Region 4820

-
Business cards:

Dean Walcott
Managing Director
Phone: 08 9417 2630
Mobile: 0471 356 802
Email: deanw@redfernworkforce.com.au
Address: 147 Tolmer Road
-
Its a new manpower (Recruitment Agency) that employs blue collar workers eg: fitters, welders, drivers and warehouse people

If you need any further information please contact myself

Cheers

Dean

```html
<!DOCTYPE html>
<html lang="en">
<head>
<meta charset="utf-8">
<title>Red Fern Workforce – DL Envelopes</title>
<link href="https://fonts.googleapis.com/css2?family=Arimo:wght@400;700&display=swap" rel="stylesheet">
<style>
  :root {
    --backdrop: #e9eaec;
    --paper: #f7f7f8;
    --paper-edge: #d9dadd;
    --brand-blue: #1d5ba8;
    --band-black: #161616;
    --ink: #2a2a2a;
    --window: #eceded;
    --window-edge: #cfd0d2;
    --flap-line: #dedfe2;
  }
  * { box-sizing: border-box; margin: 0; padding: 0; }
  html, body { width: 1200px; height: 960px; overflow: hidden; }
  body {
    background: var(--backdrop);
    font-family: "Arimo", Arial, sans-serif;
    position: relative;
  }
  .envelope {
    position: absolute;
    width: 740px;
    height: 370px;
    background: var(--paper);
    border: 1px solid var(--paper-edge);
    box-shadow: 0 10px 24px rgba(0,0,0,0.12);
    overflow: hidden;
  }
  .envelope--back { left: 400px; top: 60px; }
  .envelope--front { left: 60px; top: 520px; }

  .brand {
    display: flex;
    align-items: center;
    gap: 12px;
  }
  .brand__dot {
    width: 30px; height: 30px;
    border-radius: 50%;
    background: var(--brand-blue);
    flex: none;
  }
  .brand__name {
    color: var(--brand-blue);
    font-weight: 700;
    font-size: 20px;
    letter-spacing: 5px;
    text-transform: uppercase;
    white-space: nowrap;
  }

  /* back of envelope */
  .flap {
    position: absolute;
    left: 14px; right: 14px; top: 10px;
    height: 70px;
    border: 1px solid var(--flap-line);
    border-top: none;
    border-radius: 0 0 14px 14px;
  }
  .back-mark {
    position: absolute;
    left: 0; right: 0; top: 150px;
    display: flex;
    flex-direction: column;
    align-items: center;
    gap: 12px;
  }
  .website {
    font-size: 15px;
    color: var(--ink);
    letter-spacing: 0.3px;
  }

  /* front of envelope */
  .front-brand { position: absolute; left: 36px; top: 30px; }
  .return-address {
    position: absolute;
    left: 36px; top: 80px;
    display: flex; align-items: center; gap: 8px;
    font-size: 12px;
    color: var(--ink);
    white-space: nowrap;
  }
  .return-address svg { flex: none; }
  .address-window {
    position: absolute;
    left: 36px; top: 108px;
    width: 300px; height: 110px;
    background: var(--window);
    border: 1px solid var(--window-edge);
    border-radius: 12px;
  }
  .footer-bands {
    position: absolute;
    left: 0; bottom: 0;
    width: 740px; height: 70px;
  }
  .branches {
    position: absolute;
    right: 18px; bottom: 44px;
    color: #fff;
    font-size: 13px;
    line-height: 16px;
    letter-spacing: 0.5px;
    white-space: nowrap;
  }
</style>
</head>
<body>

  <section class="envelope envelope--back" aria-label="Envelope back">
    <div class="flap"></div>
    <div class="back-mark">
      <div class="brand">
        <span class="brand__dot"></span>
        <span class="brand__name">Red Fern Workforce</span>
      </div>
      <p class="website">www.redfernworkforce.com.au</p>
    </div>
  </section>

  <section class="envelope envelope--front" aria-label="Envelope front">
    <div class="brand front-brand">
      <span class="brand__dot"></span>
      <span class="brand__name">Red Fern Workforce</span>
    </div>
    <p class="return-address">
      <svg width="14" height="14" viewBox="0 0 14 14" aria-hidden="true">
        <circle cx="7" cy="7" r="7" fill="#1d5ba8"/>
        <path d="M7 3.2a2.3 2.3 0 0 0-2.3 2.3C4.7 7.3 7 10.5 7 10.5s2.3-3.2 2.3-5A2.3 2.3 0 0 0 7 3.2z" fill="#fff"/>
      </svg>
      147 Tolmer Road Harrowdene Coastal Region 4820
    </p>
    <div class="address-window"></div>
    <svg class="footer-bands" viewBox="0 0 740 70" aria-hidden="true">
      <rect x="0" y="34" width="740" height="36" fill="var(--band-black)"/>
      <rect x="0" y="26" width="510" height="3" fill="var(--brand-blue)"/>
      <polygon points="490,34 506,4 740,4 740,34" fill="var(--brand-blue)"/>
    </svg>
    <p class="branches">Calder | Ridgeford</p>
  </section>

</body>
</html>
```